Lumo Vessa Wigs " Styling Foam"

I need a label created for my product . The bottle size is 50ml so it must be designed to fit that size bottle. I will post my logo and examples of my bottle size. I want the label design to be simple and cute. ill also add pictures of my website, so you can get ideas from there. The bottle is white so I want the main colors to be white and pink. All colors on the label must match my logo. I love glitter as well.

I know for sure I want my logo big, and I want "Styling Foam'',
then under styling foam I would like " Medium Hold" in a different front. be very creative.

Then under that I would like it to say " No Alcohol , Saulfate or Paraben

please make sure on the label in the front it has "NET: 7.0 oz / 200g" so people know what size it is.

I would like a glitter border on the label.

I also want the back of the label to have directions.

And ingredients list too . Very small not too big at all.

Target Market(s)

My target market is woman of all ages .. but mainly woman from ages 26-65

Industry/Entity Type

Hair And Beauty

Font styles to use
Serif
Sans Serif
Decorative
Script

Colors
e667a6
eda3c7
f9d9e8
e34297

Requirements
Must have
• The project must match the colors of my logo, it must have a nice pretty glitter border . It must be simple and clean . But still stylish ! I don’t want everything after my logo to be in the same font . Have fun with this design, be creative. My logo and “ Styling Foam” must be the two centerpiece!
Nice to have
• It will be nice to have different fonts! And nice to have all the colors that match my logo
Must be expensive looking !!
Very eye catching!
Should not have
• Do not add colors that my logo doesn’t have !!!!
I don’t want it to look too plain and boring ! I want it to be classy and expensive looking !

```html
<!DOCTYPE html>
<html lang="en">
<head>
<meta charset="UTF-8">
<title>Lumo Vessa Wigs – Styling Foam Label</title>
<link href="https://fonts.googleapis.com/css2?family=DM+Serif+Display&family=Oswald:wght@500&family=Montserrat:wght@700&display=swap" rel="stylesheet">
<style>
  :root {
    --backdrop: #e9e6ea;
    --label-white: #ffffff;
    --pink-deep: #e34297;
    --pink-main: #e667a6;
    --pink-soft: #eda3c7;
    --pink-blush: #f9d9e8;
    --ink-grey: #555457;
    --ink-dark: #1e1e1e;
  }
  * { margin: 0; padding: 0; box-sizing: border-box; }
  html, body {
    width: 1200px;
    height: 975px;
    overflow: hidden;
    background: var(--backdrop);
  }
  .canvas {
    position: relative;
    width: 1200px;
    height: 975px;
  }
  .label {
    position: absolute;
    left: 420px;
    top: 87px;
    width: 360px;
    height: 800px;
    background: var(--label-white);
    box-shadow: 0 2px 10px rgba(0,0,0,0.08);
  }
  .brand-name {
    position: absolute;
    top: 72px;
    width: 100%;
    text-align: center;
    font-family: "DM Serif Display", serif;
    font-size: 33px;
    line-height: 1;
    color: var(--pink-deep);
  }
  .product-title {
    position: absolute;
    top: 168px;
    width: 100%;
    text-align: center;
    font-family: "DM Serif Display", serif;
    font-size: 50px;
    line-height: 0.92;
    color: var(--pink-deep);
    letter-spacing: 0.5px;
  }
  .pattern-panel {
    position: absolute;
    left: 66px;
    top: 288px;
    width: 229px;
    height: 228px;
    background: var(--pink-soft);
  }
  .hold-level {
    position: absolute;
    top: 536px;
    width: 100%;
    text-align: center;
    font-family: "Oswald", sans-serif;
    font-weight: 500;
    font-size: 40px;
    line-height: 1;
    color: var(--ink-grey);
    letter-spacing: 0.5px;
  }
  .free-from {
    position: absolute;
    top: 593px;
    left: 0;
    width: 100%;
    display: flex;
    justify-content: center;
    gap: 8px;
  }
  .free-from svg { width: 42px; height: 42px; }
  .net-weight {
    position: absolute;
    top: 658px;
    width: 100%;
    text-align: center;
    font-family: "Montserrat", sans-serif;
    font-weight: 700;
    font-size: 14px;
    color: var(--ink-dark);
  }
</style>
</head>
<body>
<main class="canvas">
  <section class="label">
    <h1 class="brand-name">Lumo Vessa Wigs</h1>
    <h2 class="product-title">styling<br>foam</h2>
    <div class="pattern-panel" role="img" aria-label="Pink panel with white flowing bubble line pattern"></div>
    <p class="hold-level">MEDIUM HOLD</p>
    <div class="free-from">
      <svg viewBox="0 0 42 42" role="img" aria-label="No alcohol">
        <circle cx="21" cy="21" r="20" fill="var(--pink-deep)"/>
        <rect x="16" y="16" width="9" height="15" rx="2" fill="none" stroke="#fff" stroke-width="1.6"/>
        <rect x="18.5" y="10" width="4" height="6" fill="none" stroke="#fff" stroke-width="1.6"/>
        <line x1="10" y1="10" x2="32" y2="32" stroke="#fff" stroke-width="1.8"/>
      </svg>
      <svg viewBox="0 0 42 42" role="img" aria-label="No sulfate or paraben">
        <circle cx="21" cy="21" r="20" fill="var(--pink-deep)"/>
        <path d="M17 11 h8 M18 11 v7 l-5 11 h16 l-5 -11 v-7" fill="none" stroke="#fff" stroke-width="1.6" stroke-linejoin="round"/>
        <line x1="10" y1="10" x2="32" y2="32" stroke="#fff" stroke-width="1.8"/>
      </svg>
    </div>
    <p class="net-weight">NET: 7.0 oz / 200g</p>
  </section>
</main>
</body>
</html>
```